VeloNest Crowdfunding Website 1st Page

I am looking to have a first page created for a new crowd funding website that knocks down the biggest hurdle that creative types and start ups face, legal costs. For creative projects and innovative products, we are providing intellectual property and certain other legal services wrapped into the project costs.

I am using a white label crowdfunding platform that that has a standard look and feel of most crowdfunding sites e.g. tiles with campaigns, listing of campaigns categories, create new campaign options, and donate to campaigns etc. The white label program is branded with the VeloNest logo and colors. At present there is a front page that is just a place holder for someone at ArtHive's great design! What I need is an eye-catching first page that visually and through content optimizes the VeloNest brand. (There should be space for content for those looking to raise money and those looking to donate to campaigns.)

www.pledgewave.example is, of course, the reigning King of crowdfunding. They have been so successful that they no longer have to entice people to launch campaigns there. (So they don't speak as much to those looking to raise money.) Unlike Pledgewave, of the challenges is that I have two customers I need to engage. The first is the potential crowdfund campaign owner who is looking to raise money. The second customer is the donor.

I am looking for a smart page from a marketing standpoint that also grabs you. One should feel the energy of "the crowd" when they look at the page.

Some information regarding the logo: The font is Kabel BK BT. The primary blue is R33, G121, B 159. Hex21799F and the primary greenis R179, G210, B54 Hex B3D236. The third file is a slight variation on the VN logo that you are free to use as well. (Unfortunately, I don't have all the color information for that one readily available.) If you need more files, please just let me know.

Industry/Entity Type

Marketing

Font styles to use
Other font styles liked:
• Kabel Bk BT or complimentary

Requirements
Must have
• Please use the slogan "Where the crowd meets great ideas".

```html
<!DOCTYPE html>
<html lang="en">
<head>
<meta charset="utf-8">
<title>VeloNest – Where the crowd meets great ideas</title>
<link rel="stylesheet" href="https://fonts.googleapis.com/css2?family=Questrial&family=Open+Sans:ital,wght@0,400;0,600;0,700;1,400&family=Oswald:wght@400&display=swap">
<style>
:root{
  --blue:#21799F;
  --blue-bright:#2b90c4;
  --blue-deep:#1d6d96;
  --green:#B3D236;
  --green-dark:#98b82a;
  --ink:#3a3d40;
  --text:#5d6166;
  --muted:#8f9499;
  --line:#dfe2e4;
  --panel:#f0f0f0;
  --dark:#3a3e41;
  --darker:#2d3033;
  --white:#ffffff;
  --red:#d8403a;
  --social:#3b5590;
}
*{box-sizing:border-box;margin:0;padding:0}
html,body{width:1200px;height:3842px;overflow:hidden}
body{font-family:"Open Sans",Arial,sans-serif;color:var(--text);background:var(--white);position:relative}
.display{font-family:"Questrial",Arial,sans-serif}
a{color:inherit;text-decoration:none}
section,header,footer{position:absolute;left:0;width:1200px}

/* header */
.site-header{top:0;height:148px;background:var(--white)}
.brand{position:absolute;left:104px;top:30px;display:flex;flex-direction:column;align-items:center;gap:8px}
.brand-dot{width:58px;height:58px;border-radius:50%;background:var(--blue)}
.brand-name{font-family:"Questrial",sans-serif;font-size:28px;color:var(--blue)}
.main-nav{position:absolute;left:378px;top:82px;display:flex;gap:26px;font-size:12px;color:var(--ink);text-transform:uppercase}
.main-nav .active{border-bottom:2px solid var(--ink);padding-bottom:4px}
.header-actions{position:absolute;left:727px;top:78px;display:flex;gap:9px}
.pill{height:32px;padding:0 14px 0 8px;display:flex;align-items:center;gap:8px;color:var(--white);font-size:11px;text-transform:uppercase;border-radius:2px}
.pill i{width:18px;height:18px;border-radius:50%;background:rgba(255,255,255,.35);display:block}
.pill.create{background:var(--green);width:168px}
.pill.login{background:var(--blue-bright);width:169px}

/* hero */
.hero{top:148px;height:732px;color:var(--white);overflow:hidden}
.hero-photo{position:absolute;inset:0;background:linear-gradient(90deg,#3b3a37 0%,#55483c 35%,#6b4a33 60%,#3a2a21 100%)}
.hero-shade{position:absolute;inset:0;background:linear-gradient(180deg,rgba(0,0,0,.25),rgba(0,0,0,.05) 50%,rgba(0,0,0,.35))}
.hero-title{position:absolute;top:30px;width:100%;text-align:center;font-size:46px;letter-spacing:.5px}
.hero-pitch{position:absolute;left:124px;top:270px;font-size:35px;line-height:46px;font-weight:400}
.btn-support{position:absolute;left:124px;top:384px;width:226px;height:48px;background:var(--green);font-size:24px;display:flex;align-items:center;justify-content:center}
.hero-stats{position:absolute;left:124px;top:482px;display:flex;font-size:12px;line-height:17px}
.hero-stats div{padding:0 18px;border-left:1px solid rgba(255,255,255,.6);text-align:center}
.hero-stats div:first-child{border-left:0;padding-left:4px}
.hero-stats hr{display:none}
.hero-bar{position:absolute;left:124px;top:526px;width:430px;height:2px;background:rgba(255,255,255,.4)}
.hero-bar span{display:block;width:95%;height:100%;background:var(--white)}
.hero-share{position:absolute;left:124px;top:586px;display:flex;align-items:center;gap:16px;font-size:13px;font-weight:600}
.hero-share i{width:14px;height:14px;border-radius:50%;background:var(--white);display:block}
.arrow{position:absolute;width:40px;height:70px}
.hero .arrow{top:368px}
.arrow.left{left:50px}.arrow.right{right:50px}

/* projects */
.projects{top:880px;height:1020px;background:linear-gradient(180deg,var(--blue-bright) 0%,#2a85b8 60%,var(--blue-deep) 100%)}
.tab-bar{position:absolute;left:121px;top:-40px;width:952px;height:100px;background:#3d4245;display:flex;align-items:center}
.tab{height:100%;padding:0 42px;display:flex;align-items:center;color:#b9bfc4;font-size:14px;text-transform:uppercase;letter-spacing:.5px}
.tab.active{background:#555b5f;color:var(--white)}
.search{position:absolute;right:30px;top:34px;width:280px;height:34px;background:#2f3335;border:1px solid #53595d;color:#8a9095;font-size:12px;padding:9px 12px}
.search svg{position:absolute;right:10px;top:8px}
.card{position:absolute;width:207px;height:340px;background:var(--white);box-shadow:0 3px 8px rgba(0,0,0,.25);padding:8px}
.card-photo{height:145px}
.card h3{font-family:"Questrial",sans-serif;font-weight:400;color:var(--green-dark);font-size:15px;text-align:center;margin-top:10px;white-space:nowrap;overflow:hidden}
.card p{font-size:11px;line-height:14px;color:var(--muted);margin:6px 8px 0}
.ring{display:block;margin:10px auto 0}
.card-stats{position:absolute;left:8px;right:8px;bottom:10px;border-top:1px solid var(--line);padding-top:8px;display:flex;justify-content:space-between;font-size:10px;line-height:13px;color:var(--muted)}
.card-stats b{display:block;color:var(--ink);font-size:11px}
.ribbon{position:absolute;left:-8px;top:14px;width:90px;height:22px;background:var(--green);color:var(--white);font-size:9px;font-weight:700;text-transform:uppercase;text-align:center;line-height:22px;transform:rotate(-40deg);transform-origin:50% 50%}
.ribbon.red{background:var(--red)}
.btn-more{position:absolute;left:490px;top:896px;width:222px;height:54px;background:var(--green);color:var(--white);font-size:21px;display:flex;align-items:center;justify-content:center}

/* discover */
.discover{top:1900px;height:473px;background:var(--white);text-align:center}
.discover h2{font-family:"Questrial",sans-serif;font-weight:400;font-size:32px;color:var(--ink);margin-top:50px}
.discover .hint{font-style:italic;font-size:14px;color:var(--muted);margin-top:16px}
.friends-collage{position:absolute;left:183px;top:228px;width:408px;height:148px;background:linear-gradient(90deg,#e9ecee,#cfd5d9 40%,#b6bec4 60%,#e9ecee)}
.btn-social{position:absolute;left:644px;top:275px;width:362px;height:62px;background:var(--social);color:var(--white);font-family:"Oswald",sans-serif;font-size:24px;display:flex;align-items:center;justify-content:center;gap:14px}
.btn-social i{width:26px;height:26px;background:var(--white);display:block}

/* stories */
.stories{top:2373px;height:553px;background:var(--panel);text-align:center}
.stories h2{font-family:"Questrial",sans-serif;font-weight:400;font-size:30px;color:var(--blue);margin-top:52px}
.stories .arrow{top:176px}
.story-person{position:absolute;left:372px;top:190px;text-align:left;font-size:13px;line-height:16px}
.story-person b{color:var(--green-dark);font-weight:600}
.story-person span{display:block;color:var(--blue);font-size:11px}
.story-photo{position:absolute;left:512px;top:116px;width:176px;height:176px;border-radius:50%;border:7px solid var(--white);box-shadow:0 0 0 1px var(--line);background:radial-gradient(circle at 50% 45%,#c887b0,#7f9d6a 70%)}
.story-org{position:absolute;left:735px;top:186px;display:flex;align-items:center;gap:8px;font-family:"Questrial",sans-serif;font-size:15px;color:var(--blue);text-align:left;line-height:16px}
.story-org i{width:22px;height:22px;background:var(--green);display:block}
.story-pointer{position:absolute;left:0;top:322px;width:1200px;height:20px}
.stories h3{position:absolute;top:358px;width:100%;font-family:"Oswald",sans-serif;font-weight:400;font-size:28px;color:var(--ink)}
.stories .quote{position:absolute;left:290px;top:414px;width:620px;font-size:12px;line-height:16px;font-style:italic;color:var(--text)}

/* share */
.share-love{top:2926px;height:274px;text-align:center}
.share-love h2{font-family:"Questrial",sans-serif;font-weight:400;font-size:32px;color:var(--blue);margin-top:50px}
.share-actions{position:absolute;top:144px;left:352px;display:flex;align-items:center;gap:22px}
.share-btn{width:216px;height:42px;color:var(--white);display:flex;align-items:baseline;justify-content:center;gap:6px;font-size:22px;padding-top:8px}
.share-btn small{font-size:12px}
.share-btn.create{background:var(--green)}
.share-btn.give{background:var(--blue)}
.share-or{font-family:"Questrial",sans-serif;font-size:26px;color:var(--ink)}

/* partners */
.partners{top:3200px;height:228px;background:var(--dark);text-align:center}
.partners h2{font-family:"Questrial",sans-serif;font-weight:400;font-size:30px;color:var(--white);margin-top:36px}
.partner-row{position:absolute;top:128px;left:128px;width:950px;display:flex;justify-content:space-between;align-items:center}
.partner-row span{display:block;background:#e7e8e9}
.partner-row .wide{width:80px;height:24px}
.partner-row .sq{width:44px;height:44px}
.partner-row .round{width:50px;height:50px;border-radius:50%}

/* footer */
.site-footer{top:3428px;height:355px;background:var(--panel)}
.footer-col{position:absolute;top:64px;font-size:12px;line-height:17px}
.footer-col h4{font-family:"Questrial",sans-serif;font-weight:400;font-size:21px;color:var(--ink);margin-bottom:20px}
.footer-col p{color:var(--muted);font-size:11px;line-height:15px;margin-bottom:14px}
.footer-col ul{list-style:none}
.footer-col li{color:var(--text);font-size:11px;line-height:23px;padding-left:14px;position:relative}
.footer-col li::before{content:"";position:absolute;left:0;top:10px;width:4px;height:4px;border-radius:50%;background:var(--muted)}
.footer-col.posts li{line-height:15px;margin-bottom:12px}
.footer-col.posts li::before{top:6px}
.subscribe{display:flex;margin-top:4px}
.subscribe span{width:150px;height:30px;border:1px solid var(--line);background:var(--white);font-size:10px;color:var(--muted);padding:8px}
.subscribe b{width:62px;height:30px;background:var(--green);color:var(--white);font-size:11px;display:flex;align-items:center;justify-content:center;font-weight:600}
.footer-social{display:flex;gap:10px;justify-content:flex-end;margin-top:18px;width:212px}
.footer-social i{width:13px;height:13px;border-radius:50%;background:var(--ink);display:block}
.bottom-bar{top:3783px;height:59px;background:var(--darker);color:#b4b8bb;font-size:11px}
.bottom-bar .copy{position:absolute;left:128px;top:22px}
.bottom-bar nav{position:absolute;right:128px;top:22px;display:flex;gap:26px}
</style>
</head>
<body>

<header class="site-header">
  <a class="brand" href="#"><span class="brand-dot"></span><span class="brand-name">VeloNest</span></a>
  <nav class="main-nav"><a class="active" href="#">Home</a><a href="#">Browse</a><a href="#">How it works</a></nav>
  <div class="header-actions">
    <a class="pill create" href="#"><i></i>Create a campaign</a>
    <a class="pill login" href="#"><i></i>Login / Register</a>
  </div>
</header>

<section class="hero">
  <div class="hero-photo" role="img" aria-label="Photo of a young child leaning on a table in a classroom"></div>
  <div class="hero-shade"></div>
  <h1 class="hero-title display" style="font-weight:400">Where the crowd meets great ideas</h1>
  <p class="hero-pitch display">We need your support<br>to educate, feed and accomodate!</p>
  <a class="btn-support display" href="#">Support</a>
  <div class="hero-stats">
    <div>95%<br>Funded</div>
    <div>$5,415.00<br>Pledged</div>
    <div>$12,000.00<br>Goal</div>
    <div>30<br>Backers</div>
    <div>36/28<br>Days to go</div>
  </div>
  <div class="hero-bar"><span></span></div>
  <div class="hero-share">SHARE <i></i><i></i><i></i><i></i><i></i><i></i></div>
  <svg class="arrow left" viewBox="0 0 40 70"><polyline points="32,4 6,35 32,66" fill="none" stroke="#fff" stroke-width="2"/></svg>
  <svg class="arrow right" viewBox="0 0 40 70"><polyline points="8,4 34,35 8,66" fill="none" stroke="#fff" stroke-width="2"/></svg>
</section>

<section class="projects">
  <div class="tab-bar">
    <span class="tab active">Staff picks</span>
    <span class="tab">Recently added</span>
    <span class="tab">Popular</span>
    <div class="search">Search for more Projects
      <svg width="16" height="16" viewBox="0 0 16 16"><circle cx="6.5" cy="6.5" r="5" fill="none" stroke="#2b90c4" stroke-width="2"/><line x1="10" y1="10" x2="15" y2="15" stroke="#2b90c4" stroke-width="2"/></svg>
    </div>
  </div>

  <article class="card" style="left:118px;top:104px">
    <div class="card-photo" role="img" aria-label="Black and white portrait of an old man" style="background:linear-gradient(135deg,#9a9a9a,#3d3d3d)"></div>
    <span class="ribbon">Funded</span>
    <h3>The lonely man</h3>
    <p>Morbi vel est augue mattis ultricies non et mauris. Phasellus rhoncus eusi.</p>
    <svg class="ring" width="42" height="42" viewBox="0 0 42 42"><circle cx="21" cy="21" r="16" fill="none" stroke="#dfe2e4" stroke-width="5"/><circle cx="21" cy="21" r="16" fill="none" stroke="#21799F" stroke-width="5" stroke-dasharray="100.5 100.5" transform="rotate(-90 21 21)"/></svg>
    <div class="card-stats"><span><b>100%</b>Funded</span><span><b>$6,351.00</b>Pledged</span><span><b>249 Days</b>to go</span></div>
  </article>

  <article class="card" style="left:370px;top:104px">
    <div class="card-photo" role="img" aria-label="Photo of feet in sneakers on a pavement" style="background:linear-gradient(135deg,#e3e5e8,#9aa4b0)"></div>
    <h3>Stepping the art</h3>
    <p>Morbi vel est augue mattis ultricies non et mauris. Phasellus rhoncus eusi.</p>
    <svg class="ring" width="42" height="42" viewBox="0 0 42 42"><circle cx="21" cy="21" r="16" fill="none" stroke="#dfe2e4" stroke-width="5"/><circle cx="21" cy="21" r="16" fill="none" stroke="#21799F" stroke-width="5" stroke-dasharray="10 100.5" transform="rotate(-90 21 21)"/></svg>
    <div class="card-stats"><span><b>10%</b>Funded</span><span><b>$2,590.00</b>Pledged</span><span><b>6</b>Days to go</span></div>
  </article>

  <article class="card" style="left:620px;top:104px">
    <div class="card-photo" role="img" aria-label="Photo of a small frog on a white surface" style="background:linear-gradient(135deg,#f2f2ee,#8f9a6a)"></div>
    <h3>The frog in the paintin...</h3>
    <p>Morbi vel est augue mattis ultricies non et mauris. Phasellus rhoncus eusi.</p>
    <svg class="ring" width="42" height="42" viewBox="0 0 42 42"><circle cx="21" cy="21" r="16" fill="none" stroke="#dfe2e4" stroke-width="5"/><circle cx="21" cy="21" r="16" fill="none" stroke="#21799F" stroke-width="5" stroke-dasharray="73 100.5" transform="rotate(-90 21 21)"/></svg>
    <div class="card-stats"><span><b>73%</b>Funded</span><span><b>$51,801.00</b>Pledged</span><span><b>2221</b>Days to go</span></div>
  </article>

  <article class="card" style="left:872px;top:104px">
    <div class="card-photo" role="img" aria-label="Photo of a crowd at a concert under purple lights" style="background:linear-gradient(135deg,#6d5a8c,#2e2440)"></div>
    <span class="ribbon">Funded</span>
    <h3>Concert in Huston</h3>
    <p>Morbi vel est augue mattis ultricies non et mauris. Phasellus rhoncus eusi.</p>
    <svg class="ring" width="42" height="42" viewBox="0 0 42 42"><circle cx="21" cy="21" r="16" fill="none" stroke="#21799F" stroke-width="5"/></svg>
    <div class="card-stats"><span><b>125%</b>Funded</span><span><b>$12,000</b>Pledged</span><span><b>321</b>Days to go</span></div>
  </article>

  <article class="card" style="left:118px;top:486px">
    <div class="card-photo" role="img" aria-label="Black and white portrait of a young man in glasses" style="background:linear-gradient(135deg,#8a8a8a,#2a2a2a)"></div>
    <h3>Hipster the movie</h3>
    <p>Morbi vel est augue mattis ultricies non et mauris. Phasellus rhoncus eusi.</p>
    <svg class="ring" width="42" height="42" viewBox="0 0 42 42"><circle cx="21" cy="21" r="16" fill="none" stroke="#dfe2e4" stroke-width="5"/><circle cx="21" cy="21" r="16" fill="none" stroke="#21799F" stroke-width="5" stroke-dasharray="10 100.5" transform="rotate(-90 21 21)"/></svg>
    <div class="card-stats"><span><b>10%</b>Funded</span><span><b>$2,500</b>Pledged</span><span><b>248</b>to go</span></div>
  </article>

  <article class="card" style="left:370px;top:486px">
    <div class="card-photo" role="img" aria-label="Black and white photo of a busy underground station" style="background:linear-gradient(135deg,#b0b0b0,#3a3a3a)"></div>
    <span class="ribbon red">Popular</span>
    <h3>Underground photography</h3>
    <p>Morbi vel est augue mattis ultricies non et mauris. Phasellus rhoncus eusi.</p>
    <svg class="ring" width="42" height="42" viewBox="0 0 42 42"><circle cx="21" cy="21" r="16" fill="none" stroke="#dfe2e4" stroke-width="5"/><circle cx="21" cy="21" r="16" fill="none" stroke="#21799F" stroke-width="5" stroke-dasharray="33 100.5" transform="rotate(-90 21 21)"/></svg>
    <div class="card-stats"><span><b>33%</b>Funded</span><span><b>$15,000</b>Pledged</span><span><b></b></span></div>
  </article>

  <article class="card" style="left:620px;top:486px">
    <div class="card-photo" role="img" aria-label="Dark photo of a man standing in a doorway" style="background:linear-gradient(135deg,#6a5644,#241c16)"></div>
    <span class="ribbon">Funded</span>
    <h3>New episode of the comi...</h3>
    <p>Morbi vel est augue mattis ultricies non et mauris. Phasellus rhoncus eusi.</p>
    <svg class="ring" width="42" height="42" viewBox="0 0 42 42"><circle cx="21" cy="21" r="16" fill="none" stroke="#21799F" stroke-width="5"/></svg>
    <div class="card-stats"><span><b>175%</b>Funded</span><span><b>$8,200</b>Pledged</span><span><b>316</b>Days to go</span></div>
  </article>

  <article class="card" style="left:872px;top:486px">
    <div class="card-photo" role="img" aria-label="Photo of railway tracks through an autumn forest" style="background:linear-gradient(135deg,#d08a3c,#5a3a22)"></div>
    <h3>Expedition in Vienna</h3>
    <p>Morbi vel est augue mattis ultricies non et mauris. Phasellus rhoncus eusi.</p>
    <svg class="ring" width="42" height="42" viewBox="0 0 42 42"><circle cx="21" cy="21" r="16" fill="none" stroke="#dfe2e4" stroke-width="5"/><circle cx="21" cy="21" r="16" fill="none" stroke="#21799F" stroke-width="5" stroke-dasharray="73 100.5" transform="rotate(-90 21 21)"/></svg>
    <div class="card-stats"><span><b>73%</b>Funded</span><span><b>$15,000</b>Pledged</span><span><b>321</b>Days to go</span></div>
  </article>

  <a class="btn-more" href="#">View More</a>
</section>

<section class="discover">
  <h2>Discover great projects with your friends!</h2>
  <p class="hint">Want to learn more? See how it works</p>
  <div class="friends-collage" role="img" aria-label="Mosaic of friends' profile pictures on grey tiles"></div>
  <a class="btn-social" href="#"><i></i>Connect with Linkspace</a>
</section>

<section class="stories">
  <h2>Success Stories</h2>
  <svg class="arrow left" viewBox="0 0 40 70" style="left:124px"><polyline points="30,14 12,35 30,56" fill="none" stroke="#3a3d40" stroke-width="2"/></svg>
  <svg class="arrow right" viewBox="0 0 40 70" style="right:124px"><polyline points="10,14 28,35 10,56" fill="none" stroke="#3a3d40" stroke-width="2"/></svg>
  <div class="story-person"><b>Dana Whitfield</b><span>Project Manager</span></div>
  <div class="story-photo" role="img" aria-label="Portrait photo of the project manager outdoors"></div>
  <div class="story-org"><i></i><span>Riverbend<br><small style="font-size:9px">Rehabilitation Center</small></span></div>
  <svg class="story-pointer" viewBox="0 0 1200 20"><polyline points="0,1 580,1 600,19 620,1 1200,1" fill="var(--white)" stroke="#cfd3d6" stroke-width="1"/></svg>
  <h3>Thanks to make my rehabilitation center green</h3>
  <p class="quote">Lorem ipsum dolor sit amet, consectetur adipiscing elit. Aliquam aliquaerat at sodales pharetra. Morbi et est enim. Fusce fringilla dui non fermentum, in laoreet volutpat orci et consequat. Curabitur semper ac lacus luctus. In egestas, mi ut sodales sollicitudin, purus orci placerat tortor, suscipit leo ligula ac justo. Nam tristique nec velit in vulputate.</p>
</section>

<section class="share-love">
  <h2>Share the love</h2>
  <div class="share-actions">
    <a class="share-btn create" href="#">Create <small>a fundraiser</small></a>
    <span class="share-or">OR</span>
    <a class="share-btn give" href="#">Give <small>a fundraiser</small></a>
  </div>
</section>

<section class="partners">
  <h2>Our Partners</h2>
  <div class="partner-row">
    <span class="wide"></span><span class="wide"></span><span class="sq"></span><span class="wide"></span><span class="round"></span><span class="wide"></span><span class="round"></span><span class="wide"></span>
  </div>
</section>

<footer class="site-footer">
  <div class="footer-col" style="left:127px;width:200px">
    <h4>Why we rock!</h4>
    <p>Lorem ipsum dolor sit amet, conseq adipiscing elit. Praesent id nisi lacus sed gravida leo, sollicitudin quis eget.</p>
    <p>Lorem ipsum dolor sit amet, conseq adipiscing elit. Praesent id nisi lacus sed gravida leo, sollicitudin quis eget tempor. Donec nulla elit orci id lacus.</p>
  </div>
  <div class="footer-col" style="left:393px;width:150px">
    <h4>Categories</h4>
    <ul><li>Art</li><li>Comics</li><li>Design</li><li>Film &amp; Video</li><li>Games</li><li>Music</li><li>Photography</li><li>Technology</li></ul>
  </div>
  <div class="footer-col posts" style="left:570px;width:240px">
    <h4>Latest posts</h4>
    <ul>
      <li>Default Post with Featured Image<br>October 3rd, 2013</li>
      <li>Post without Sidebar<br>October 3rd, 2013</li>
      <li>Post with an External Video<br>October 1st, 2013</li>
      <li>Markup: HTML Tags and Formatting<br>September 23rd, 2013</li>
    </ul>
  </div>
  <div class="footer-col" style="left:848px;width:230px">
    <h4>Get in touch</h4>
    <p>Nam aliquet, velit quis consequat elementum, odio tellus vestibulum.</p>
    <div class="subscribe"><span>Enter your email here</span><b>Submit</b></div>
    <div class="footer-social"><i></i><i></i><i></i><i></i><i></i></div>
  </div>
</footer>

<footer class="bottom-bar">
  <span class="copy">© 2014 VeloNest - All Rights Reserved</span>
  <nav><a href="#">Sitemap</a><a href="#">Terms and Conditions</a><a href="#">Privacy Policy</a></nav>
</footer>

</body>
</html>
```